Retail Appliance Store Chain needs NEW business Card

Name of my company is Brandon's Appliances brandonsappliances.com is our website. . We are a 2 location brick and mortar, and online store selling premium, luxury, and normal household appliances, such as ovens, stoves, cooktops, dishwashers, refrigerators, washers and dryers, grills, air conditioners etc. The focus is on large kitchen appliances and laundry appliances.
Please visit http://brandonsappliances.com to get a feel for the business and branding.
I have attached the Brandon's Appliances logo (i do not have eps or psd or ai). And I have also attached our current business cards that we use. We have two versions. A double sided version for managers, and a one side version for regular employees.
Please submit BOTH one sided and two sided designs if possible.
Please keep consistent with the Brandon's Appliances logo, colors, etc.
I would prefer no rounded corners on the business card designs for printing costs.
Information on the cards (in no particular order):
Name - Employee Name
Business name - Brandon's Appliances
website - brandonsappliances.com
Email - Employee Email
2 Phone Numbers - store 1 address, store 2 address
2 Addresses - store 1 address, store 2 address

*do NOT need Fax #

Industry/Entity Type

Home Appliance

Contact Information for Business Card

Logo - Brandons Appliances Logo
Name - Employee Name
Email - Employee Email

Please no rounded corners. Standard US Business Card Size please.

Font styles to use
Serif
Sans Serif

Requirements
Must have
• colors and design that somewhat match the feel of current logo and website
Should not have
• No rounded corners.
No non-traditional business card size. US Standard Business Card Size only

```html
<!DOCTYPE html>
<html lang="en">
<head>
<meta charset="utf-8">
<title>Brandon's Appliances – Business Card</title>
<link href="https://fonts.googleapis.com/css2?family=Montserrat:wght@500;600;700&display=swap" rel="stylesheet">
<style>
  :root {
    --brand-blue: #21508c;
    --brand-blue-deep: #1a4278;
    --card-white: #ffffff;
    --backdrop: #e6e8eb;
    --text-on-blue: #f2f5fa;
  }
  * { box-sizing: border-box; margin: 0; padding: 0; }
  html, body {
    width: 1200px;
    height: 900px;
    overflow: hidden;
    background: var(--backdrop);
    font-family: "Montserrat", Arial, sans-serif;
  }
  .business-card {
    position: absolute;
    left: 75px;
    top: 150px;
    width: 1050px;
    height: 600px;
    background: var(--card-white);
    box-shadow: 0 10px 30px rgba(0,0,0,0.12);
    overflow: hidden;
  }
  .brand-name {
    position: absolute;
    right: 70px;
    top: 70px;
    color: var(--brand-blue);
    font-weight: 700;
    font-size: 38px;
    letter-spacing: 0.5px;
    white-space: nowrap;
  }
  .employee-name {
    position: absolute;
    left: 80px;
    top: 238px;
    color: var(--brand-blue);
    font-weight: 500;
    font-size: 34px;
    letter-spacing: 2px;
    text-transform: uppercase;
    white-space: nowrap;
  }
  .contact-band {
    position: absolute;
    left: 0;
    top: 300px;
    width: 100%;
    height: 240px;
    background: linear-gradient(90deg, var(--brand-blue-deep), var(--brand-blue));
  }
  .contact-list {
    position: absolute;
    left: 110px;
    top: 26px;
    list-style: none;
    color: var(--text-on-blue);
    font-weight: 600;
    font-size: 24px;
    letter-spacing: 1.5px;
    line-height: 1.3;
  }
  .contact-item {
    display: flex;
    align-items: center;
    margin-bottom: 14px;
    white-space: nowrap;
  }
  .contact-icon {
    width: 22px;
    height: 22px;
    margin-right: 22px;
    flex-shrink: 0;
  }
  .contact-item.address { align-items: flex-start; }
  .contact-item.address .contact-icon { margin-top: 18px; }
</style>
</head>
<body>
  <div class="business-card">
    <div class="brand-name">Brandon's Appliances</div>
    <div class="employee-name">Daniel Reed</div>
    <div class="contact-band">
      <ul class="contact-list">
        <li class="contact-item">
          <svg class="contact-icon" viewBox="0 0 24 24" fill="none" stroke="currentColor" stroke-width="2" stroke-linejoin="round"><path d="M5 3h4l2 5-2.5 1.5a11 11 0 0 0 6 6L16 13l5 2v4a2 2 0 0 1-2 2A17 17 0 0 1 3 5a2 2 0 0 1 2-2z"/></svg>
          <span>(555) 014-7365</span>
        </li>
        <li class="contact-item address">
          <svg class="contact-icon" viewBox="0 0 24 24" fill="currentColor"><path d="M12 2a7 7 0 0 0-7 7c0 5 7 13 7 13s7-8 7-13a7 7 0 0 0-7-7zm0 9.5A2.5 2.5 0 1 1 12 6.5a2.5 2.5 0 0 1 0 5z"/></svg>
          <span>148 Harbor Mill Rd.<br>Ashford, CT 06278</span>
        </li>
        <li class="contact-item">
          <svg class="contact-icon" viewBox="0 0 24 24" fill="none" stroke="currentColor" stroke-width="2" stroke-linejoin="round"><rect x="3" y="5" width="18" height="14"/><path d="M3 6l9 7 9-7"/></svg>
          <span>danielr@brandonsappliances.com</span>
        </li>
        <li class="contact-item">
          <svg class="contact-icon" viewBox="0 0 24 24" fill="none" stroke="currentColor" stroke-width="2"><circle cx="12" cy="12" r="9"/><path d="M3 12h18M12 3c3 3 3 15 0 18M12 3c-3 3-3 15 0 18"/></svg>
          <span>www.brandonsappliances.com</span>
        </li>
      </ul>
    </div>
  </div>
</body>
</html>
```